Builder and developer needs website

I am re-establishing my building company after 15 years of managing other peoples building companies.
My main focus is building medium density housing with other investors as part of a syndicate. My current website is hopeless and cant be found by Google or Yahoo. It is www.tobrinbuildworks.net.au

I have a couple of websites that I have seen that are a good inspiration for me.

I have looked at the Orlet Developments site http://www.orlet.com.au/ and like what I see. They offer the same development service that I want to offer. I also want to have a membership page/area for trades.
• The site is not wordy. It is glam and emotive
• The links to each page are easy to see and follow.
• The home page has the large images at the bottom that direct you into the emotional areas i.e. what we are building, discover the possibilities and expression of interest.
• The “Services” page is great. No long stories. Just click on the image you want to read about and off you go.
• There are a few links that don’t direct you to the correct pages i.e. expression of interest.
• There are a few places where they capture your contact details.

Also the property strategies page http://www.homewardvantage.net/steady-home-vantage of the SHV site is very relevant to my goals. This site has a similar message but is far wordier explaining it. The research part of me likes this site as it explains more. It also uses emotive description.
The one annoying thing is the “Holdings Accelerant” sends you to a page with no tabs above to move to another page and “Estate Brainhouse” sends you to another site. I suppose his aim is to get paying people to his education courses and into his syndicates.

There is also Dale Pemberton’s site http://dalepembertonestates.com.au/services/ It is hard to read due to the colours. Again it is wordy, but it is educational.

My preference is using the template of the Orlet “services” page and each wordy piece is a link.
Updates

Hello Contestants

My old website was for my old profile as a builder only. Now I want to be seen as a builder and developer as per the Orlet web site. I will be developing property just like that site and the SHV site and the Dale Pemberton site. Thanks

Regards
Glenn Toller

Target Market(s)

Target market is people that want an investment property portfolio.
Have a SMSF or Self Managed Super Fund and want property to diversify their portfolio.
People wanting to aim for early retirement and spending time with family or working for worthwhile causes.
Have a reasonable risk profile.
Have imagination and can see how a syndicate works and the benefits for everyone.
Have imagination and can picture the finished product.
Prefer not to pay retail for property.
Prepared to wait for units to be constructed.
People that want others/joint partners around them to be come wealthy as well.

Industry/Entity Type

Education

Requirements
Nice to have
• Clear and easy navigation of the web site.
The site will be used by people in their late 30's upwards.
Sophistication
Easy maintenance of the site by me. I have limited skills in this department.
Easy SEO finding as my current site is hopeless
A members page for investors
A way of getting emails for a data base.
Should not have
• Flashing lights.
Spelling errors.
Loud noises
Background that makes the text difficult to read.

```html
<!DOCTYPE html>
<html lang="en">
<head>
<meta charset="utf-8">
<title>Tobrin Buildworks</title>
<link rel="stylesheet" href="https://fonts.googleapis.com/css2?family=Arimo:wght@400;700&display=swap">
<style>
:root{
  --blue:#0d6cb5;
  --blue-dark:#0a5a98;
  --green:#2fae78;
  --green-dark:#249866;
  --ink:#111;
  --grey-btn:#3a3a3a;
  --footer:#1f1f1f;
  --header-bg:#f7f7f7;
  --frame:#3fb6e8;
  --icon:#5a5a5a;
}
*{box-sizing:border-box;margin:0;padding:0}
html,body{width:1130px;height:1200px;overflow:hidden;background:#fff}
body{font-family:"Arimo",Arial,sans-serif;color:var(--ink);position:relative}
.site-header{position:absolute;top:0;left:0;width:1130px;height:102px;background:var(--header-bg)}
.brand{position:absolute;left:95px;top:26px;display:flex;align-items:center;gap:10px}
.brand-mark{width:30px;height:30px;background:var(--blue)}
.brand-name{font-size:30px;font-weight:700;color:var(--blue);letter-spacing:.2px}
.main-nav{position:absolute;right:87px;top:0;height:102px;display:flex}
.main-nav a{display:flex;align-items:center;height:102px;padding:0 18px;font-size:14px;color:#222;text-decoration:none}
.main-nav a.active{background:linear-gradient(var(--blue),var(--blue-dark));color:#fff;font-weight:700;width:88px;justify-content:center;padding:0}
.hero{position:absolute;top:102px;left:0;width:1130px;height:372px;background:linear-gradient(180deg,#ecebe7 0%,#d9cdbd 45%,#b88a5c 75%,#8e6a48 100%)}
.hero-arrow{position:absolute;top:173px;width:20px;height:30px;background:rgba(255,255,255,.85)}
.hero-arrow.prev{left:0;border-radius:0 4px 4px 0}
.hero-arrow.next{right:0;border-radius:4px 0 0 4px}
.hero-arrow svg{display:block;margin:8px auto}
.hero-dots{position:absolute;left:515px;bottom:0;width:118px;height:26px;background:rgba(255,255,255,.6);border-radius:8px 8px 0 0;display:flex;justify-content:center;align-items:center;gap:7px}
.hero-dots span{width:12px;height:12px;border-radius:50%;background:#888;box-shadow:inset 0 1px 2px rgba(0,0,0,.4)}
.hero-dots span.on{background:var(--blue)}
.newsletter{position:absolute;top:474px;left:0;width:1130px;height:111px;background:linear-gradient(var(--green),var(--green-dark) 50%,var(--green))}
.newsletter h2{position:absolute;left:97px;top:30px;font-size:17px;font-weight:700;color:#fff}
.newsletter p{position:absolute;left:96px;top:63px;font-size:11px;color:#111}
.field{position:absolute;top:36px;width:177px;height:33px;background:#fff;border-radius:3px;box-shadow:0 2px 3px rgba(0,0,0,.25);font-size:11px;padding:11px 13px;color:#222}
.field.name{left:537px}
.field.email{left:742px}
.signup{position:absolute;left:942px;top:36px;width:100px;height:34px;background:var(--grey-btn);border-radius:3px;color:#fff;font-size:17px;display:flex;align-items:center;justify-content:center}
.welcome{position:absolute;top:604px;left:96px;width:674px}
.welcome h1{font-size:17px;font-weight:400;margin-bottom:16px}
.welcome p{font-size:11px;line-height:21px;text-align:justify}
.badges{position:absolute;top:608px;left:797px}
.badge{position:absolute;background:#e4e4e4}
.badge.wide{left:0;top:0;width:248px;height:50px;background:#2b6b3c;border-radius:4px}
.badge.small{left:0;top:64px;width:45px;height:56px;background:#d9c27a}
.badge.mid{left:70px;top:64px;width:105px;height:46px;background:#d8d8d8}
.services{position:absolute;top:780px;left:95px;width:948px;display:flex;justify-content:space-between}
.service{width:305px;position:relative;height:300px}
.service-photo{width:305px;height:151px;border:2px solid var(--frame)}
.service h3{font-size:17px;font-weight:400;margin:26px 0 10px}
.service p{font-size:11px;line-height:21px;text-align:justify;padding:0 2px}
.more{position:absolute;right:2px;top:271px;width:72px;height:30px;background:var(--grey-btn);color:#fff;font-size:17px;display:flex;align-items:center;justify-content:center}
.photo-crane{background:linear-gradient(180deg,#e7b878 0%,#e0995a 55%,#2a1d14 85%)}
.photo-framing{background:linear-gradient(160deg,#8aa6c6 0%,#d8b07a 45%,#b98050 100%)}
.photo-safety{background:linear-gradient(150deg,#b89262 0%,#e0c79f 50%,#ddd8d0 100%)}
.site-footer{position:absolute;top:1113px;left:0;width:1130px;height:87px;background:var(--footer)}
.footer-links{position:absolute;left:97px;top:17px;font-size:11px;color:#eee}
.footer-links span{margin:0 5px}
.copyright{position:absolute;left:96px;top:50px;font-size:11px;color:#bbb}
.social{position:absolute;left:854px;top:29px;display:flex;gap:10px}
.social span{width:30px;height:30px;border-radius:50%;background:var(--icon)}
</style>
</head>
<body>
<header class="site-header">
  <div class="brand"><span class="brand-mark"></span><span class="brand-name">Tobrin Buildworks</span></div>
  <nav class="main-nav">
    <a class="active" href="#">Home</a>
    <a href="#">About us</a>
    <a href="#">Services</a>
    <a href="#">Getting Started</a>
    <a href="#">Gallery</a>
    <a href="#">Contact</a>
  </nav>
</header>

<section class="hero" role="img" aria-label="Modern open-plan living room interior with timber panelling, kitchen and ceiling fans">
  <div class="hero-arrow prev"><svg width="8" height="14" viewBox="0 0 8 14"><path d="M7 1 1 7l6 6" fill="none" stroke="#666" stroke-width="2"/></svg></div>
  <div class="hero-arrow next"><svg width="8" height="14" viewBox="0 0 8 14"><path d="M1 1l6 6-6 6" fill="none" stroke="#666" stroke-width="2"/></svg></div>
  <div class="hero-dots"><span></span><span></span><span class="on"></span><span></span><span></span><span></span></div>
</section>

<section class="newsletter">
  <h2>JOIN NEWSLETTER..</h2>
  <p>Please enter your name &amp; email to join Orlet Development free Newsletter :</p>
  <div class="field name">Name</div>
  <div class="field email">Email Address</div>
  <div class="signup">SIGN UP</div>
</section>

<section class="welcome">
  <h1>Welcome To Tobrin Buildworks</h1>
  <p>Tobrin Buildworks provides site development and project management expertise across all forms of residential construction including duplexes, townhouse complexes and blocks of units. Tobrin Buildworks will treat you as their partner and take responsibility for your site as if it was their own, ensuring your peace of mind throughout the project.Constructions will treat you as their partner and take responsibility for your site as if it was their own, ensuring your peace of mind throughout the project.Constructions will treat you as their partner and take responsibility for your site as if it was their own, ensuring your peace of</p>
</section>

<aside class="badges" aria-label="Industry memberships">
  <div class="badge wide"></div>
  <div class="badge small"></div>
  <div class="badge mid"></div>
</aside>

<section class="services">
  <article class="service">
    <div class="service-photo photo-crane" role="img" aria-label="Construction workers silhouetted against a sunset with a crane"></div>
    <h3>Constructions</h3>
    <p>Tobrin Buildworks provides site development and project management expertise across all forms of residential construction including duplexes, townhouse complexes</p>
    <a class="more">More</a>
  </article>
  <article class="service">
    <div class="service-photo photo-framing" role="img" aria-label="Two builders in hard hats reviewing plans inside a timber house frame"></div>
    <h3>Residential Development</h3>
    <p>Tobrin Buildworks provides site development and project management expertise across all forms of residential construction including duplexes, townhouse complexes</p>
    <a class="more">More</a>
  </article>
  <article class="service">
    <div class="service-photo photo-safety" role="img" aria-label="Safety glasses and dust mask resting on timber"></div>
    <h3>Commercial Development</h3>
    <p>Tobrin Buildworks provides site development and project management expertise across all forms of residential construction including duplexes, townhouse complexes</p>
    <a class="more">More</a>
  </article>
</section>

<footer class="site-footer">
  <div class="footer-links">Site map<span>|</span>Disclaimer &amp; Privacy Policy<span>|</span>Contact us</div>
  <div class="copyright">©&nbsp; 2014 Tobrin Buildworks Ltd</div>
  <div class="social" aria-label="Social links"><span></span><span></span><span></span><span></span><span></span></div>
</footer>
</body>
</html>
```